Fernvale Business Card Design

We are looking for a fresh business card design for our new logo. We would like a business card that is unique but friendly. We are in the window coverings business offering blinds, shutters and shades for homes.

Target Market(s)

Targeting the end-consumer

Industry/Entity Type

Business

Requirements
Must have
• Must have a dedicates space for a photo of our sales person. Must contain our new logo (attached).

```html
<!DOCTYPE html>
<html lang="en">
<head>
<meta charset="utf-8">
<title>Fernvale Business Card</title>
<link rel="stylesheet" href="https://fonts.googleapis.com/css2?family=EB+Garamond:ital,wght@0,400;0,500;1,400&family=Marcellus&display=swap">
<style>
  :root {
    --stage: #e4e3e3;
    --front-top: #8e8a8a;
    --front-bottom: #726e6e;
    --leaf-green: #93c83e;
    --ink: #3a3535;
    --frame: #5a5252;
    --paper: #ffffff;
  }
  * { box-sizing: border-box; margin: 0; padding: 0; }
  html, body { width: 1200px; height: 750px; overflow: hidden; }
  body {
    background: var(--stage);
    position: relative;
    font-family: "EB Garamond", Georgia, serif;
  }
  .card {
    position: absolute;
    top: 232px;
    width: 500px;
    height: 286px;
    border-radius: 22px;
    overflow: hidden;
    box-shadow: 0 10px 26px rgba(0,0,0,0.16);
  }
  /* Front side */
  .card-front {
    left: 60px;
    background: linear-gradient(160deg, var(--front-top), var(--front-bottom));
    color: var(--paper);
  }
  .brand {
    position: absolute;
    left: 70px;
    top: 100px;
    display: flex;
    align-items: center;
    gap: 22px;
  }
  .brand-mark {
    width: 58px;
    height: 58px;
    border: 3px solid var(--paper);
    border-radius: 6px;
  }
  .brand-name {
    font-family: "Marcellus", Georgia, serif;
    font-size: 58px;
    letter-spacing: 1px;
    line-height: 1;
  }
  .front-web {
    position: absolute;
    left: 0; right: 0;
    bottom: 36px;
    text-align: center;
    font-size: 17px;
    letter-spacing: 0.5px;
  }
  /* Back side */
  .card-back {
    left: 640px;
    background: var(--paper);
    border: 2px solid var(--leaf-green);
    color: var(--ink);
  }
  .name-band {
    position: absolute;
    left: -2px;
    top: 32px;
    width: 290px;
    height: 50px;
    background: var(--leaf-green);
    border-radius: 0 25px 25px 0;
    padding-left: 26px;
    display: flex;
    align-items: center;
    font-family: "Marcellus", Georgia, serif;
    color: var(--paper);
    font-size: 27px;
    letter-spacing: 0.5px;
  }
  .position {
    position: absolute;
    left: 66px;
    top: 86px;
    font-size: 15px;
    letter-spacing: 1px;
    color: var(--leaf-green);
  }
  .contact {
    position: absolute;
    left: 24px;
    top: 124px;
    list-style: none;
    font-size: 13px;
    line-height: 1.35;
  }
  .contact li {
    display: flex;
    align-items: flex-start;
    gap: 10px;
    margin-bottom: 6px;
  }
  .contact svg { width: 18px; height: 18px; flex: none; fill: var(--ink); }
  .photo-slot {
    position: absolute;
    right: 34px;
    top: 30px;
    width: 150px;
    height: 128px;
    border: 5px solid var(--frame);
    display: flex;
    align-items: center;
    justify-content: center;
    text-align: center;
    font-family: "Marcellus", Georgia, serif;
    font-size: 15px;
    line-height: 1.2;
    color: var(--frame);
  }
  .corner-panel {
    position: absolute;
    right: -2px;
    bottom: -2px;
    width: 210px;
    height: 110px;
    background: var(--leaf-green);
    border-radius: 60px 0 0 0;
    display: flex;
    align-items: center;
    justify-content: center;
    font-family: "Marcellus", Georgia, serif;
    font-size: 30px;
    color: var(--paper);
  }
</style>
</head>
<body>
  <section class="card card-front" aria-label="Business card front">
    <div class="brand">
      <span class="brand-mark"></span>
      <span class="brand-name">Fernvale</span>
    </div>
    <p class="front-web">www.fernvale.com</p>
  </section>

  <section class="card card-back" aria-label="Business card back">
    <h1 class="name-band">JANE M. ROWE</h1>
    <p class="position">POSITION</p>
    <ul class="contact">
      <li>
        <svg viewBox="0 0 24 24" aria-hidden="true"><path d="M6.6 10.8a15 15 0 0 0 6.6 6.6l2.2-2.2a1 1 0 0 1 1-.25 11.4 11.4 0 0 0 3.6.57 1 1 0 0 1 1 1V20a1 1 0 0 1-1 1A17 17 0 0 1 3 4a1 1 0 0 1 1-1h3.5a1 1 0 0 1 1 1c0 1.25.2 2.45.57 3.57a1 1 0 0 1-.25 1z"/></svg>
        <span>+123456789</span>
      </li>
      <li>
        <svg viewBox="0 0 24 24" aria-hidden="true"><path fill="none" stroke="#3a3535" stroke-width="2" d="M12 2a10 10 0 1 0 0 20a10 10 0 1 0 0-20M2 12h20M12 2c3 3 3 17 0 20M12 2c-3 3-3 17 0 20"/></svg>
        <span>jane.rowe@fernvale.com</span>
      </li>
      <li>
        <svg viewBox="0 0 24 24" aria-hidden="true"><path d="M12 2a7 7 0 0 0-7 7c0 5 7 13 7 13s7-8 7-13a7 7 0 0 0-7-7zm0 9.5a2.5 2.5 0 1 1 0-5 2.5 2.5 0 0 1 0 5z"/></svg>
        <span>Unit 1234, Tower<br>3rd St cor. 5th Ave<br>State, USA, 123456</span>
      </li>
    </ul>
    <div class="photo-slot">PICTURE<br>GOES<br>HERE</div>
    <div class="corner-panel">Fernvale</div>
  </section>
</body>
</html>
```